TGV Electricial Contracting Services

Hi guys, after a design for my small electrical company, have logo design files to be incorporated into the layout, the basic concept is electrical contracting services for residential, commercial, industrial & data services, image is clean clear and strong,

Card format is to have a nice clean logo on front,with maybe the Residential – commercial – industrial - data, followed with licensed & insured, followed by contact details on backside of the card.

Target Market(s)

Residential, commercial, industrial sectors.

Industry/Entity Type

Electrical

Contact Information for Business Card

TGV logo,
Residential – commercial – industrial - data
REC: 57310
Email: tgv@wavolink.net.au
Phone: 0472 358 129

Requirements
Must have
• Clean & strong design.
Nice to have
• If possible, I would like the logo colours inverted so the text is orange and the background is black on the front of the card, then the backside of the card be the reverse colour
Should not have
• No Sparks, lightning bolts,

```html
<!DOCTYPE html>
<html lang="en">
<head>
<meta charset="utf-8">
<title>TGV Electricial Contracting Services – Business Card</title>
<link rel="stylesheet" href="https://fonts.googleapis.com/css2?family=Michroma&display=swap">
<style>
  :root {
    --orange: #f07f1e;
    --orange-light: #f59a3e;
    --orange-deep: #e06a12;
    --black: #111111;
    --white: #ffffff;
    --page: #e9e6e1;
    --card-w: 640px;
    --card-h: 372px;
  }
  * { box-sizing: border-box; margin: 0; padding: 0; }
  html, body {
    width: 1200px;
    height: 900px;
    overflow: hidden;
    background: var(--page);
    font-family: "Michroma", sans-serif;
  }
  .sheet {
    position: relative;
    width: 1200px;
    height: 900px;
    display: flex;
    flex-direction: column;
    align-items: center;
    justify-content: center;
    gap: 40px;
  }
  .card {
    position: relative;
    width: var(--card-w);
    height: var(--card-h);
    overflow: hidden;
    box-shadow: 0 6px 18px rgba(0,0,0,0.25);
  }
  .card-art {
    position: absolute;
    inset: 0;
    width: 100%;
    height: 100%;
  }

  /* ---------- Brand lockup ---------- */
  .brand {
    position: absolute;
    display: flex;
    flex-direction: column;
  }
  .brand-mark {
    font-size: 74px;
    line-height: 1;
    letter-spacing: -2px;
  }
  .brand-name {
    font-size: 15px;
    letter-spacing: 0.5px;
    margin-top: 6px;
  }

  /* ---------- Back card ---------- */
  .card--back .brand {
    top: 26px;
    right: 48px;
    align-items: flex-start;
  }
  .card--back .brand-mark,
  .card--back .brand-name { color: var(--black); }
  .services {
    position: absolute;
    left: 32px;
    bottom: 60px;
    color: var(--orange);
    font-size: 13px;
    line-height: 1.6;
    letter-spacing: 0.4px;
  }

  /* ---------- Front card ---------- */
  .card--front .brand {
    top: 40px;
    left: 44px;
  }
  .card--front .brand-mark { color: var(--orange); }
  .card--front .brand-name { color: var(--white); }
  .holder {
    position: absolute;
    right: 36px;
    top: 238px;
    text-align: right;
  }
  .holder-name {
    font-size: 20px;
    color: var(--black);
  }
  .holder-role {
    font-size: 10px;
    color: var(--white);
    margin-top: 4px;
  }
  .contact-list {
    position: absolute;
    left: 30px;
    top: 282px;
    list-style: none;
  }
  .contact-list li {
    display: flex;
    align-items: center;
    gap: 14px;
    color: var(--black);
    font-size: 15px;
    line-height: 26px;
  }
  .contact-list li.contact-email { font-size: 13px; }
  .contact-icon { width: 16px; height: 16px; flex: none; }
</style>
</head>
<body>
<main class="sheet">

  <!-- Back of card -->
  <section class="card card--back" aria-label="Business card back">
    <svg class="card-art" viewBox="0 0 640 372" preserveAspectRatio="none" aria-hidden="true">
      <defs>
        <linearGradient id="back-orange" x1="0" y1="0" x2="1" y2="0">
          <stop offset="0" stop-color="var(--orange-deep)"/>
          <stop offset="1" stop-color="var(--orange-light)"/>
        </linearGradient>
      </defs>
      <rect width="640" height="372" fill="var(--black)"/>
      <polygon points="0,0 640,0 640,150 250,186 0,154" fill="url(#back-orange)"/>
      <polygon points="250,186 640,150 640,160 252,196" fill="var(--white)"/>
    </svg>
    <div class="brand">
      <span class="brand-mark">TGV</span>
      <span class="brand-name">Tolman Grey Vance Electrical</span>
    </div>
    <p class="services">
      licenced &amp; insured Residential<br>
      commercial – industrial – data REC: 57310
    </p>
  </section>

  <!-- Front of card -->
  <section class="card card--front" aria-label="Business card front">
    <svg class="card-art" viewBox="0 0 640 372" preserveAspectRatio="none" aria-hidden="true">
      <defs>
        <linearGradient id="front-orange" x1="0" y1="0" x2="1" y2="0">
          <stop offset="0" stop-color="var(--orange-deep)"/>
          <stop offset="1" stop-color="var(--orange-light)"/>
        </linearGradient>
      </defs>
      <rect width="640" height="372" fill="url(#front-orange)"/>
      <polygon points="0,0 640,0 640,34 420,200 0,250" fill="var(--black)"/>
      <polygon points="640,44 640,58 426,224 0,274 0,260 422,210" fill="var(--white)"/>
      <polygon points="640,58 640,64 428,230 0,280 0,274 426,224" fill="var(--black)"/>
      <rect x="0" y="346" width="330" height="14" fill="var(--white)"/>
      <rect x="330" y="336" width="310" height="12" fill="var(--black)"/>
    </svg>
    <div class="brand">
      <span class="brand-mark">TGV</span>
      <span class="brand-name">Tolman Grey Vance Electrical</span>
    </div>
    <div class="holder">
      <p class="holder-name">Dale Harper</p>
      <p class="holder-role">Owner</p>
    </div>
    <ul class="contact-list">
      <li class="contact-phone">
        <svg class="contact-icon" viewBox="0 0 16 16" aria-hidden="true">
          <path d="M4 1 L6.5 1 L7 4.5 L5.3 5.6 C6 7.6 8.4 10 10.4 10.7 L11.5 9 L15 9.5 L15 12 C15 13.6 13.6 15 12 15 C6 15 1 10 1 4 C1 2.4 2.4 1 4 1 Z" fill="var(--white)"/>
        </svg>
        <span>0472 358 129</span>
      </li>
      <li class="contact-email">
        <svg class="contact-icon" viewBox="0 0 16 16" aria-hidden="true">
          <rect x="1" y="3" width="14" height="10" fill="none" stroke="var(--white)" stroke-width="1.4"/>
          <polyline points="1,3 8,9 15,3" fill="none" stroke="var(--white)" stroke-width="1.4"/>
        </svg>
        <span>tgv@wavolink.net.au</span>
      </li>
    </ul>
  </section>

</main>
</body>
</html>
```